Business card

I need a business card design for my consulting company in animal welfare for livestock. I like clean, crisp, simple.

One I imagined was double-sided:
side1: just my name and contact information
side2: silhouette of farm animals. Could be 3 (pig, cow, chicken) or all the species (pig, cow, chicken, duck, sheep, rabbit, etc) that continue the length of the card. I have attached an image of a silhouette style.

But, I am open to any concept.

Industry/Entity Type

Business

```html
<!DOCTYPE html>
<html lang="en">
<head>
<meta charset="utf-8">
<title>Humane Advisory for Farm Animal Producers – Business Card</title>
<link rel="stylesheet" href="https://fonts.googleapis.com/css2?family=Fira+Sans:wght@500&family=Inter:wght@300&display=swap">
<style>
  :root {
    --card-blue: #0a4bd8;
    --title-green: #3fcf44;
    --name-green: #8fd12f;
    --contact-green: #4fe020;
    --tone-green: #30d030;
    --tone-lime: #98f010;
    --tone-teal: #3fb0c0;
    --tone-sky: #41b6f2;
    --tone-navy: #0526c4;
  }
  * { margin: 0; padding: 0; box-sizing: border-box; }
  html, body {
    width: 1200px;
    height: 741px;
    overflow: hidden;
    background: var(--card-blue);
  }
  .card {
    position: relative;
    width: 1200px;
    height: 741px;
    background: var(--card-blue);
    overflow: hidden;
  }
  .corner-pattern {
    position: absolute;
  }
  .corner-pattern--top-left {
    left: 0;
    top: 0;
    width: 155px;
    height: 372px;
    background: linear-gradient(180deg, var(--tone-green) 0%, var(--tone-teal) 35%, var(--tone-green) 70%, #1a3fb0 100%);
  }
  .corner-pattern--bottom-right {
    left: 973px;
    top: 406px;
    width: 227px;
    height: 335px;
    background: linear-gradient(180deg, var(--tone-navy) 0%, var(--tone-teal) 35%, var(--tone-sky) 55%, var(--tone-green) 100%);
  }
  .company {
    position: absolute;
    left: 221px;
    top: 112px;
    font-family: "Fira Sans", sans-serif;
    font-weight: 500;
    font-size: 76px;
    line-height: 74px;
    color: var(--title-green);
    letter-spacing: 0.5px;
  }
  .person {
    position: absolute;
    left: 221px;
    top: 300px;
    font-family: "Inter", sans-serif;
    font-weight: 300;
    color: var(--contact-green);
  }
  .person-name {
    font-size: 68px;
    line-height: 80px;
    color: var(--name-green);
    letter-spacing: -0.5px;
  }
  .person-contact {
    font-size: 43px;
    line-height: 49px;
    letter-spacing: -0.3px;
  }
  .animals {
    position: absolute;
    left: 68px;
    top: 505px;
    width: 240px;
    height: 214px;
    border-radius: 40px 30px 20px 60px;
    background: linear-gradient(160deg, #8ccf30 0%, #5cc8a8 55%, #41b4f0 100%);
  }
</style>
</head>
<body>
<div class="card">
  <div class="corner-pattern corner-pattern--top-left" role="img" aria-label="Decorative cluster of overlapping translucent green and blue squares"></div>
  <div class="corner-pattern corner-pattern--bottom-right" role="img" aria-label="Decorative cluster of overlapping translucent blue and green squares"></div>

  <h1 class="company">Humane Advisory for<br>Farm Animal Producers</h1>

  <div class="person">
    <p class="person-name">Helen Marwick</p>
    <p class="person-contact">Email: helen.marwick@fieldmail.com</p>
    <p class="person-contact">Tel: +1 604 555 0172</p>
  </div>

  <div class="animals" role="img" aria-label="Overlapping silhouettes of a cow, pig, chicken and rabbit in green and blue tones"></div>
</div>
</body>
</html>
```